After-School Program - End of the Year Mailing to Donors

We would like to highlight some of our accomplishments from the year and ask people to donate to our organization. We are a non-profit organization that serves underprivileged children with after school programs. We want a 6x9 flyer with printing on both sides that we can mail out soon. The flyer should be a mix of great photos, some text, and a space for mailing and return address.

Target Market(s)

regular donors

Industry/Entity Type

Education

Font styles to use
Serif

Colors

Designer to choose colors to be used in the design.

Requirements
Must have
• Photos, text, a space on one side for a mailing label, a return address, and a stamp.
Nice to have
• attractive, eye-catching
Should not have
• boring

```html
<!DOCTYPE html>
<html lang="en">
<head>
<meta charset="utf-8">
<title>Eastside Kids Learning House – Donor Postcard</title>
<link href="https://fonts.googleapis.com/css2?family=Oswald:wght@500;600&family=Raleway:wght@400;500;700&display=swap" rel="stylesheet">
<style>
  :root{
    --teal:#4e97a6;
    --yellow:#f3ec1e;
    --grey:#7b7b7b;
    --grey-light:#8e8e8e;
    --ink:#2b2b2b;
    --footer:#2d2d2d;
    --paper:#ffffff;
    --backdrop:#ece7df;
  }
  *{box-sizing:border-box;margin:0;padding:0}
  html,body{width:922px;height:1200px;overflow:hidden}
  body{background:var(--backdrop);font-family:'Raleway',sans-serif;position:relative}

  .card{position:absolute;left:80px;width:762px;height:506px;background:var(--paper);overflow:hidden;box-shadow:0 3px 8px rgba(0,0,0,.25)}
  .card--front{top:70px}
  .card--back{top:624px}

  /* front */
  .hero{position:absolute;left:0;top:0}
  .headline{position:absolute;right:22px;top:326px;text-align:right}
  .headline__main{font-family:'Oswald',sans-serif;font-weight:600;font-size:36px;line-height:42px;color:var(--teal);letter-spacing:.2px}
  .headline__main .muted{color:var(--grey)}
  .headline__sub{font-size:23px;line-height:28px;color:var(--grey);letter-spacing:.5px;margin-top:2px}
  .headline__accent{font-size:20.5px;line-height:26px;color:var(--teal);letter-spacing:.5px}

  .org-mark{position:absolute;left:34px;top:388px;width:150px;display:flex;align-items:center;gap:8px}
  .org-mark__dot{flex:none;width:18px;height:18px;border-radius:50%;background:var(--yellow)}
  .org-mark__name{font-weight:700;font-size:15px;line-height:18px;color:var(--ink)}

  .contact-strip{position:absolute;left:0;top:434px}
  .contact-strip__items{position:absolute;right:24px;top:444px;display:flex;gap:16px;font-size:18px;color:var(--teal);align-items:center}
  .contact-strip__items span{display:flex;align-items:center;gap:6px}

  .address-bar{position:absolute;left:0;bottom:0;width:762px;height:30px;background:var(--teal);display:flex;align-items:center;padding-left:46px;color:#fff;font-size:18px;gap:10px;white-space:nowrap}
  .address-bar strong{font-weight:700}
  .icon{display:inline-block;flex:none}

  /* back */
  .photo{position:absolute;top:0;height:134px}
  .photo--music{left:0;width:124px;background:linear-gradient(160deg,#c9c2b6,#8f7f6c 60%,#5c5048)}
  .photo--play{left:130px;width:132px;background:linear-gradient(160deg,#b7a893,#6e6a63 55%,#3f4d5c)}
  .photo--friends{left:267px;width:133px;background:linear-gradient(160deg,#9fae8f,#4f5a47 55%,#2c3a34)}

  .story{position:absolute;left:0;top:134px;width:400px;height:304px;background:var(--teal);padding:36px 22px 0 32px}
  .story__list{list-style:none;color:#fff;font-size:13.2px;line-height:17.4px}
  .story__list li{position:relative;padding-left:18px;margin-bottom:9px}
  .story__list li::before{content:"";position:absolute;left:0;top:4px;width:8px;height:8px;border-radius:50%;background:var(--yellow)}
  .story__list strong{font-weight:700}

  .story-footer{position:absolute;left:0;top:438px;width:400px;height:68px;background:var(--footer);color:#fff}
  .story-footer__org{position:absolute;left:14px;top:14px;display:flex;gap:6px}
  .story-footer__name{color:var(--yellow);font-weight:700;font-size:10.5px;line-height:14px}
  .story-footer__addr{font-size:10px;line-height:14px}
  .story-footer__contact{position:absolute;left:222px;top:12px;font-size:12.5px;line-height:22px;white-space:nowrap}
  .story-footer__contact div{display:flex;align-items:center;gap:7px}

  .mail-side .org-mark{left:430px;top:62px}
  .stamp-box{position:absolute;left:644px;top:26px;width:91px;height:87px;border:1px solid #555}
  .address-line{position:absolute;left:461px;width:273px;height:1px;background:#777}
  .address-line--1{top:282px}
  .address-line--2{top:322px}
  .address-line--3{top:362px}
</style>
</head>
<body>

<section class="card card--front">
  <svg class="hero" width="762" height="360" viewBox="0 0 762 360">
    <defs>
      <clipPath id="heroClip">
        <path d="M0,0 H762 V270 C720,285 680,300 640,294 C600,285 590,238 568,238 C540,238 520,250 496,246 C470,240 460,228 444,230 C420,232 360,250 320,282 C270,320 230,340 184,338 C110,335 40,290 0,238 Z"/>
      </clipPath>
      <linearGradient id="heroFill" x1="0" y1="0" x2="0.3" y2="1">
        <stop offset="0" stop-color="#8a8174"/>
        <stop offset=".5" stop-color="#6f6a66"/>
        <stop offset="1" stop-color="#3f4a5a"/>
      </linearGradient>
    </defs>
    <path d="M0,238 C40,290 110,335 184,338 C230,340 270,320 320,282 C360,250 420,232 444,230 C460,228 470,240 496,246 C520,250 540,238 568,238 C590,238 600,285 640,294 C680,300 720,285 762,270" fill="none" stroke="var(--teal)" stroke-width="12" transform="translate(0,7)"/>
    <path d="M0,238 C40,290 110,335 184,338 C230,340 270,320 320,282 C360,250 420,232 444,230 C460,228 470,240 496,246 C520,250 540,238 568,238 C590,238 600,285 640,294 C680,300 720,285 762,270" fill="none" stroke="var(--yellow)" stroke-width="5" transform="translate(0,3)"/>
    <rect width="762" height="360" fill="url(#heroFill)" clip-path="url(#heroClip)" role="img" aria-label="Group photo of smiling children with two adult staff members inside a sandwich shop"/>
  </svg>

  <div class="org-mark">
    <span class="org-mark__dot"></span>
    <span class="org-mark__name">Eastside Kids Learning House</span>
  </div>

  <div class="headline">
    <div class="headline__main">EDUCATIONAL <span class="muted">AND</span> COMMUNITY</div>
    <div class="headline__sub">BUILDING PROGRAMS FOR CHILDREN</div>
    <div class="headline__accent">YOUTH AND FAMILIES</div>
  </div>

  <svg class="contact-strip" width="762" height="44" viewBox="0 0 762 44">
    <path d="M0,40 H340 L376,2 H762" fill="none" stroke="var(--grey-light)" stroke-width="4"/>
  </svg>
  <div class="contact-strip__items">
    <span>
      <svg class="icon" width="18" height="18" viewBox="0 0 20 20"><circle cx="10" cy="10" r="9" fill="var(--yellow)" stroke="var(--teal)" stroke-width="1.4"/><path d="M6.5,5.5 l2,0 l1,2.5 l-1.3,1 q1,2 3,3 l1,-1.3 l2.5,1 l0,2 q-5,1 -8.2,-6.2 z" fill="var(--teal)"/></svg>
      (555) 210-4473
    </span>
    <span>
      <svg class="icon" width="18" height="18" viewBox="0 0 20 20"><circle cx="10" cy="10" r="9" fill="var(--yellow)" stroke="var(--teal)" stroke-width="1.4"/><circle cx="10" cy="10" r="5.5" fill="none" stroke="var(--teal)" stroke-width="1.2"/><path d="M4.5,10 H15.5 M10,4.5 V15.5" stroke="var(--teal)" stroke-width="1.2"/></svg>
      www.brightpathkids.org
    </span>
  </div>

  <div class="address-bar">
    <svg class="icon" width="22" height="22" viewBox="0 0 22 22"><circle cx="11" cy="11" r="10" fill="none" stroke="var(--yellow)" stroke-width="1.6"/><path d="M11,5 a4,4 0 0 1 4,4 c0,3 -4,8 -4,8 s-4,-5 -4,-8 a4,4 0 0 1 4,-4z" fill="var(--yellow)"/><circle cx="11" cy="9" r="1.5" fill="var(--teal)"/></svg>
    <strong>Eastside Kids Learning House</strong>
    <span>218 W. Alder St. Fairview, CA&nbsp; 90000</span>
  </div>
</section>

<section class="card card--back">
  <div class="photo photo--music" role="img" aria-label="Children playing violin and cello at a music recital"></div>
  <div class="photo photo--play" role="img" aria-label="Children playing together outdoors with a staff member"></div>
  <div class="photo photo--friends" role="img" aria-label="Two boys smiling on a playground"></div>

  <div class="story">
    <ul class="story__list">
      <li>Eastside Kids Learning House is in the middle of its <strong>24th</strong> year of ministry and we need your help to finish our year strong!</li>
      <li>We need another <strong>$35,000</strong> from our individual donors to help us meet our budget.</li>
      <li>We serve over <strong>150</strong> children each day at our four sites with a unique mix of homework help, a focus on literacy, enrichment classes - including music lessons, and a caring environment based on God's love.&nbsp; Please help us continue to impact children and families through our high quality faith-based educational programs.</li>
    </ul>
  </div>

  <div class="story-footer">
    <div class="story-footer__org">
      <svg class="icon" width="18" height="18" viewBox="0 0 22 22"><circle cx="11" cy="11" r="10" fill="none" stroke="var(--yellow)" stroke-width="1.6"/><path d="M11,5 a4,4 0 0 1 4,4 c0,3 -4,8 -4,8 s-4,-5 -4,-8 a4,4 0 0 1 4,-4z" fill="var(--yellow)"/></svg>
      <div>
        <div class="story-footer__name">Eastside Kids Learning House</div>
        <div class="story-footer__addr">218 W. Alder St. Fairview,<br>CA&nbsp; 90000</div>
      </div>
    </div>
    <div class="story-footer__contact">
      <div><svg class="icon" width="15" height="15" viewBox="0 0 20 20"><circle cx="10" cy="10" r="9" fill="none" stroke="var(--yellow)" stroke-width="1.6"/><path d="M6.5,5.5 l2,0 l1,2.5 l-1.3,1 q1,2 3,3 l1,-1.3 l2.5,1 l0,2 q-5,1 -8.2,-6.2 z" fill="var(--yellow)"/></svg>(555) 210-4473</div>
      <div><svg class="icon" width="15" height="15" viewBox="0 0 20 20"><circle cx="10" cy="10" r="9" fill="var(--yellow)"/><circle cx="10" cy="10" r="5.5" fill="none" stroke="var(--footer)" stroke-width="1.2"/><path d="M4.5,10 H15.5 M10,4.5 V15.5" stroke="var(--footer)" stroke-width="1.2"/></svg>www.brightpathkids.org</div>
    </div>
  </div>

  <div class="mail-side">
    <div class="org-mark">
      <span class="org-mark__dot"></span>
      <span class="org-mark__name">Eastside Kids Learning House</span>
    </div>
    <div class="stamp-box"></div>
    <div class="address-line address-line--1"></div>
    <div class="address-line address-line--2"></div>
    <div class="address-line address-line--3"></div>
  </div>
</section>

</body>
</html>
```